Broschüre für Trovimo-Coach
Sehr schnelle und professionelle Umsetzung. Die Designerin hat inhaltlich mitgedacht und die einzelnen Elemente passend und kreativ platziert. Der Kontakt war außerdem sehr nett. Sehr zu empfehlen!
Zielgruppe
Ich bin Deutschlands erster Trovimo-Coach. Ich zeige Unternehmern, Selbstständigen und Vertrieblern wie sie mit persönlichen Videobotschaften mehr Interessen und Abschlüsse generieren.
Aufgabenstellung
Es soll eine Broschüre grafisch gestaltet werden, die als eBook sowie für den Druck verwendet werden kann.
Format DIN A 4.
Bereitgestellt werden folgende Unterlagen:
(1) Texte und Grob-Struktur in der entsprechenden Reihenfolge.
(2) Die Broschüre soll sich an der Struktur des beigefügten eBooks 'Copper Lantern Drift' orientieren.
(3) Fotos, Logo und Grafikelemente sind beigefügt. Zusätzliches Bildmaterial darf eingesetzt werden.
(4) Ein 'Brand Look' mit Farben, Schriftarten und Stil-Elementen ist beigefügt.
(5) Druckvorlage gemäß beigefügter Vorlage von Papyrano. Für den Druck müssen es 20 oder 24 Seiten sein.
Bitte grafisch an meiner Website orientieren: www.haraldkunzo.de

```html
<!DOCTYPE html>
<html lang="de">
<head>
<meta charset="utf-8">
<title>Trovimo Broschüre – Umschlag</title>
<link href="https://fonts.googleapis.com/css2?family=Poppins:wght@400;500;700;800&display=swap" rel="stylesheet">
<style>
  :root {
    --bg: #e4e4e4;
    --paper: #ffffff;
    --ink-green: #0f5a3c;
    --brand-green: #2f9a5a;
    --band-olive: #a9ad36;
    --band-light: #a3cc64;
    --band-deep: #2f8460;
    --text-grey: #555a5c;
    --photo-light: #c9cbca;
    --photo-dark: #9ea2a2;
  }
  * { margin: 0; padding: 0; box-sizing: border-box; }
  html, body { width: 1200px; height: 868px; overflow: hidden; }
  body {
    background: var(--bg);
    font-family: "Poppins", sans-serif;
    display: flex;
    align-items: center;
    justify-content: center;
  }
  .spread { display: flex; box-shadow: 0 14px 40px rgba(0,0,0,.22); }
  .page {
    position: relative;
    width: 560px;
    height: 792px;
    background: var(--paper);
    overflow: hidden;
  }
  .back-cover { background: linear-gradient(90deg, #f4f4f4 0%, #ffffff 70%, #ebebeb 100%); }
  .front-cover { background: linear-gradient(90deg, #f0f0f0 0%, #ffffff 25%, #ffffff 100%); }

  /* Back cover */
  .quote-band {
    position: absolute;
    left: 0; right: 0;
    top: 236px; height: 286px;
    background: linear-gradient(90deg, var(--band-olive) 0%, var(--band-light) 50%, var(--band-deep) 100%);
    display: flex; flex-direction: column; align-items: center; justify-content: center;
    color: #fff; text-align: center;
    letter-spacing: .12em;
  }
  .quote-text { font-size: 15px; line-height: 1.55; font-weight: 400; }
  .quote-author { margin-top: 14px; font-size: 15px; }
  .brand-mark {
    display: flex; align-items: center; gap: 10px;
    color: var(--ink-green);
    font-weight: 800;
    letter-spacing: .02em;
  }
  .brand-dot { border-radius: 50%; background: var(--brand-green); flex: none; }
  .back-cover .brand-mark { position: absolute; top: 590px; left: 0; right: 0; justify-content: center; font-size: 17px; }
  .back-cover .brand-dot { width: 30px; height: 30px; }
  .contact {
    position: absolute; left: 0; right: 0; top: 680px;
    text-align: center; color: var(--text-grey);
    font-size: 13px; letter-spacing: .1em; line-height: 1.7;
  }

  /* Front cover */
  .cover-title {
    position: absolute; top: 58px; left: 0; right: 0;
    text-align: center;
    font-size: 52px; font-weight: 800;
    color: var(--ink-green);
    letter-spacing: .03em;
  }
  .cover-photo {
    position: absolute; top: 176px; left: 0; right: 0; height: 300px;
    background: radial-gradient(ellipse at 50% 40%, var(--photo-light), var(--photo-dark));
  }
  .cover-subtitle {
    position: absolute; top: 512px; left: 40px; right: 40px;
    text-align: center; color: var(--text-grey);
    font-size: 13.5px; letter-spacing: .1em; line-height: 1.4;
  }
  .divider {
    position: absolute; top: 572px; left: 140px; right: 140px;
    border-top: 1px dashed #9a9a9a;
  }
  .cover-author {
    position: absolute; top: 588px; left: 0; right: 0;
    text-align: center; font-weight: 700; font-size: 17px;
    letter-spacing: .08em; color: #1b1b1b;
  }
  .front-cover .brand-mark { position: absolute; top: 650px; left: 0; right: 0; justify-content: center; font-size: 14px; }
  .front-cover .brand-dot { width: 24px; height: 24px; }
</style>
</head>
<body>
  <main class="spread">
    <section class="page back-cover">
      <div class="quote-band">
        <p class="quote-text">„Du bist nur eine Videobotschaft<br>von Deinem nächsten Kunden entfernt.“</p>
        <p class="quote-author">– Dr. Harald W. Kunzo –</p>
      </div>
      <div class="brand-mark"><span class="brand-dot"></span><span>DR. HARALD W. KUNZO</span></div>
      <p class="contact">Dr. Harald W. Kunzo | Birkenweg 12 | 83101<br>Moosried www.haraldkunzo.de</p>
    </section>

    <section class="page front-cover">
      <h1 class="cover-title">Trovimo</h1>
      <div class="cover-photo" role="img" aria-label="Foto: Coach im blauen Pullover filmt sich mit dem Smartphone und winkt vor einer Betonwand"></div>
      <p class="cover-subtitle">5 Bausteine, wie Du mit persönlichen Videobotschaften<br>mehr Interessenten und Abschlüsse gewinnst.</p>
      <div class="divider"></div>
      <p class="cover-author">Dr. Harald W. Kunzo</p>
      <div class="brand-mark"><span class="brand-dot"></span><span>DR. HARALD W. KUNZO</span></div>
    </section>
  </main>
</body>
</html>
```